Need Kesto Ep Cover

THIS IS FOR ZEPLOR SO IT MUST LOOK GREAT IN THUMBNAIL.
I am doing an album called Kesto for all of my songs, I want it to be a faded rainbow design like the drawing filled with my pictures by the brush font in green, pink, gold and black. here are the pictures and drawing- with the rainbow.
I included some photos you may use, whatever you do make it look nice and professional and these requirements :1400 x 1400 pixels
JPG file type
72 - 300dpi (300dpi is the best)
Less than 25mb
RGB color scheme (not CMYK)
Unique to this particular title. We cannot accept artwork that has been used for another title.
and also fill in the cd pack because I want to make a cd case out of it.
Also use these fonts- MY CD CASE NEEDS MY NAME MARISOLE DUNKETT AND KESTO.
http://www.typecrate.net/helene-queen-k.font?psize=l&text=Marisole+Dunkett
http://www.typecrate.net/mtf-queen-of-sketchyland.font?psize=l&text=KESTO
http://www.typecrate.net/i-love-grunge.font?psize=l&text=KESTO
http://www.typecrate.net/vtks-contact.font?psize=l&text=KESTO
http://www.typecrate.net/dots-land-gotika.font?psize=l&text=Marisole+Dunkett
Also please fill in cd design form listed because I want to make hard copies.
Also if you feel rainbow is not professional enough just do your own thing just make sure there is a picture of me. Thank you.

Target Market(s)

Disabilities, Men in college, Young girls.

Industry/Entity Type

It Professional

Font styles to use
Decorative
Script

```html
<!DOCTYPE html>
<html lang="en">
<head>
<meta charset="utf-8">
<title>Marisole Dunkett — Kesto</title>
<link rel="stylesheet" href="https://fonts.googleapis.com/css2?family=Great+Vibes&display=swap">
<style>
  :root {
    --space-deep: #05060f;
    --space-mid: #0d1424;
    --aurora-green: #1fb07a;
    --aurora-teal: #1d7d6a;
    --nebula-pink: #b4206e;
    --nebula-violet: #3a0f3a;
    --title-teal: #2ee6c8;
    --title-teal-dark: #0b6f62;
    --title-pink: #f03fb0;
    --title-pink-dark: #7a0d55;
    --portrait-warm: #b89a7c;
    --portrait-dark: #2a2420;
  }
  html, body {
    margin: 0;
    padding: 0;
    width: 1200px;
    height: 1200px;
    overflow: hidden;
    background: var(--space-deep);
  }
  .cover {
    position: relative;
    width: 1200px;
    height: 1200px;
    overflow: hidden;
    background: radial-gradient(ellipse at 50% 40%, var(--space-mid), var(--space-deep) 75%);
  }
  .cover__sky {
    position: absolute;
    inset: 0;
  }
  .cover__portrait {
    position: absolute;
    left: 600px;
    top: 395px;
    width: 600px;
    height: 805px;
    background:
      radial-gradient(ellipse 30% 22% at 45% 30%, var(--portrait-warm), transparent 70%),
      radial-gradient(ellipse 55% 45% at 55% 60%, #7d6a58, transparent 75%),
      linear-gradient(180deg, #3b332c 0%, var(--portrait-dark) 100%);
    -webkit-mask-image: radial-gradient(ellipse 60% 60% at 55% 55%, #000 55%, transparent 100%);
    mask-image: radial-gradient(ellipse 60% 60% at 55% 55%, #000 55%, transparent 100%);
  }
  .cover__title {
    position: absolute;
    margin: 0;
    font-family: "Great Vibes", cursive;
    font-weight: 400;
    line-height: 1;
    white-space: nowrap;
  }
  .cover__artist-first,
  .cover__artist-last {
    color: var(--title-teal);
    text-shadow:
      1px 1px 0 #bffff3,
      -2px -2px 0 var(--title-teal-dark),
      4px 6px 10px rgba(0, 0, 0, 0.85);
  }
  .cover__artist-first {
    left: 30px;
    top: 60px;
    font-size: 270px;
  }
  .cover__artist-last {
    left: 60px;
    top: 440px;
    font-size: 190px;
  }
  .cover__release {
    left: 60px;
    top: 870px;
    font-size: 220px;
    color: var(--title-pink);
    text-shadow:
      1px 1px 0 #ffd0ee,
      -2px -2px 0 var(--title-pink-dark),
      4px 6px 10px rgba(0, 0, 0, 0.85);
  }
</style>
</head>
<body>
<main class="cover">
  <svg class="cover__sky" width="1200" height="1200" viewBox="0 0 1200 1200" aria-hidden="true">
    <defs>
      <radialGradient id="aurora-left" cx="0.5" cy="0.5" r="0.5">
        <stop offset="0" stop-color="var(--aurora-green)" stop-opacity="0.55"/>
        <stop offset="1" stop-color="var(--aurora-teal)" stop-opacity="0"/>
      </radialGradient>
      <radialGradient id="aurora-right" cx="0.5" cy="0.5" r="0.5">
        <stop offset="0" stop-color="var(--aurora-green)" stop-opacity="0.7"/>
        <stop offset="1" stop-color="var(--aurora-teal)" stop-opacity="0"/>
      </radialGradient>
      <radialGradient id="nebula" cx="0.5" cy="0.5" r="0.5">
        <stop offset="0" stop-color="var(--nebula-violet)" stop-opacity="0.2"/>
        <stop offset="0.6" stop-color="var(--nebula-pink)" stop-opacity="0.35"/>
        <stop offset="1" stop-color="var(--nebula-pink)" stop-opacity="0"/>
      </radialGradient>
    </defs>
    <ellipse cx="150" cy="560" rx="420" ry="260" fill="url(#aurora-left)" transform="rotate(-20 150 560)"/>
    <ellipse cx="1120" cy="640" rx="300" ry="200" fill="url(#aurora-right)" transform="rotate(-25 1120 640)"/>
    <ellipse cx="560" cy="860" rx="420" ry="360" fill="url(#nebula)"/>
    <g fill="none" stroke="var(--nebula-pink)" stroke-linecap="round">
      <path d="M360 1150 A 330 330 0 0 1 660 540" stroke-width="14" stroke-opacity="0.35"/>
      <path d="M420 1100 A 260 260 0 0 1 640 610" stroke-width="8" stroke-opacity="0.4"/>
      <path d="M470 1060 A 200 200 0 0 1 630 680" stroke-width="5" stroke-opacity="0.45"/>
    </g>
    <g fill="#ffffff">
      <circle cx="695" cy="72" r="1.8"/>
      <circle cx="120" cy="180" r="1"/>
      <circle cx="980" cy="40" r="1.2"/>
      <circle cx="1120" cy="150" r="1"/>
      <circle cx="420" cy="30" r="1"/>
      <circle cx="60" cy="700" r="1"/>
      <circle cx="1060" cy="470" r="1.2"/>
      <circle cx="300" cy="820" r="1"/>
      <circle cx="760" cy="360" r="1"/>
      <circle cx="880" cy="260" r="1"/>
      <circle cx="200" cy="1050" r="1"/>
      <circle cx="560" cy="640" r="1"/>
      <circle cx="1160" cy="320" r="1"/>
      <circle cx="30" cy="330" r="1"/>
    </g>
  </svg>

  <div class="cover__portrait" role="img" aria-label="Portrait photo of the artist, seated with arms folded, wearing a dark sparkling dress"></div>

  <h1 class="cover__title cover__artist-first">Marisole</h1>
  <p class="cover__title cover__artist-last">Dunkett</p>
  <h2 class="cover__title cover__release">Kesto</h2>
</main>
</body>
</html>
```